Coffeeshop menu for filter tip

We want to have a cannabis (coffeeshop) menu in the size 25mm wide x 60mm wide. Some examples attached.

it must have the following text:
Menu

WEED p/g
Vortigan €16
Tangerosa €14
Dusk Rover €14
Mangolina €16
Ultra Fern €14
Amber Hermit €14

HASH p/g
Nepali Bronze €12
Velvet Ember€11
Cedar Pine €14
Red Fable €10

Target Market(s)

tourist in Amsterdam

Requirements
Nice to have
• cannabis sign leaf
• No Cigarettes allowed symbol

```html
<!DOCTYPE html>
<html lang="en">
<head>
<meta charset="utf-8">
<title>Coffeeshop Menu</title>
<link rel="stylesheet" href="https://fonts.googleapis.com/css2?family=Chewy&display=swap">
<style>
  :root {
    --ink: #000000;
    --paper: #ffffff;
    --magenta: #ff1cf2;
    --yellow: #fff21a;
    --cyan: #2af3e6;
    --green: #62ff1c;
    --red: #ff1a1a;
  }
  html, body {
    margin: 0;
    padding: 0;
    width: 1200px;
    height: 2884px;
    overflow: hidden;
    background: var(--paper);
  }
  .menu-card {
    position: relative;
    width: 1200px;
    height: 2884px;
    overflow: hidden;
    font-family: "Chewy", "Arial Narrow", sans-serif;
    font-weight: 400;
    color: var(--paper);
  }
  .swirl-backdrop {
    position: absolute;
    inset: 0;
    background:
      radial-gradient(ellipse 600px 900px at 20% 30%, var(--magenta) 0%, transparent 70%),
      radial-gradient(ellipse 500px 800px at 85% 25%, var(--green) 0%, transparent 70%),
      radial-gradient(ellipse 500px 700px at 95% 55%, var(--red) 0%, transparent 70%),
      radial-gradient(ellipse 600px 700px at 10% 65%, var(--yellow) 0%, transparent 70%),
      radial-gradient(ellipse 700px 600px at 60% 70%, var(--cyan) 0%, transparent 70%),
      radial-gradient(ellipse 700px 500px at 40% 95%, var(--magenta) 0%, transparent 70%),
      linear-gradient(160deg, var(--yellow), var(--cyan) 35%, var(--magenta) 65%, var(--green));
  }
  .title-bar {
    position: absolute;
    left: 0;
    top: 0;
    width: 1200px;
    height: 358px;
    background: var(--ink);
  }
  .title-bar h1 {
    margin: 0;
    position: absolute;
    left: 70px;
    top: 10px;
    font-family: "Chewy", "Arial Narrow", sans-serif;
    font-weight: 400;
    font-size: 300px;
    line-height: 320px;
    letter-spacing: 6px;
    color: var(--paper);
  }
  .price-box {
    position: absolute;
    left: 41px;
    width: 976px;
    background: var(--ink);
    box-sizing: border-box;
    padding: 22px 0 0 34px;
    overflow: hidden;
  }
  .price-box.weed { top: 549px; height: 1058px; }
  .price-box.hash { top: 1863px; height: 773px; }
  .price-box h2 {
    margin: 0;
    font-size: 150px;
    line-height: 160px;
    font-weight: 400;
  }
  .price-box h2 .unit {
    font-size: 90px;
    letter-spacing: 2px;
  }
  .price-list {
    list-style: none;
    margin: 10px 0 0;
    padding: 0;
  }
  .price-list li {
    font-size: 100px;
    line-height: 140px;
    white-space: nowrap;
    letter-spacing: 1px;
  }
</style>
</head>
<body>
  <main class="menu-card">
    <div class="swirl-backdrop" role="img" aria-label="Psychedelic swirling background in magenta, yellow, cyan, green and red"></div>

    <header class="title-bar">
      <h1>MENU</h1>
    </header>

    <section class="price-box weed">
      <h2>Weed <span class="unit">(p/g)</span></h2>
      <ul class="price-list">
        <li>Vortigan €16</li>
        <li>Tangerosa €14</li>
        <li>Dusk Rover €14</li>
        <li>Mangolina €16</li>
        <li>Ultra Fern €14</li>
        <li>Amber Hermit €14</li>
      </ul>
    </section>

    <section class="price-box hash">
      <h2>Hash <span class="unit">(p/g)</span></h2>
      <ul class="price-list">
        <li>Nepali Bronze €12</li>
        <li>Velvet Ember €11</li>
        <li>Cedar Pine €14</li>
        <li>Red Fable €10</li>
      </ul>
    </section>
  </main>
</body>
</html>
```